ONE PAGE WEB DESIGN NEEDED for Finance Company

We need a web design (ONE PAGE DESIGN ONLY) for a new finance website called Brightwell Lending. Brightwell Lending helps customers get the right loan, whether its a home loan, investment loan, business loan etc.

You are required to come up with just the homepage design. Professionalism and quality is the key factors in the successful design.

Here are a few design questions to help you out:

-
What information should be used on the page?
Ive provided a document which outlines all the information needed to put on homepage (attached to the brief - called brightwell_page_info). Also see the Must Have section below on this brief.

-
What links should appear in the navigation/footer?:
The navigation should provide links to the following pages (NOTE: services link has subcategories):
1 Homepage
2 Services
- Home loans
- Investment loans
- Refinancing loans
- Business loans
3 About Us
4 FAQ
5 Contact Us

-
What colors should be used in the design?
Our company colors - Cyan: #2EADE3, Blue: #004B70, White. Feel free to submit designs with slight variations if you feel it improves the design.

-
What should the layout of the page be?
This is up to you to come up with - we are open to different layouts for the page design (as long as they capture the information effectively and making it easy to understand).

Target Market(s)

Potential Home owners, Families and Business Owners

Industry/Entity Type

Business

Requirements
Must have
• - Must contain our logo (attached as PNG and Illustrator file)
- Winning designer must supply a Photoshop file (PSD) that will allow us.
Nice to have
• - Should include photos/images of families, professional groups, tradespeople etc (you can use stock photos from PixQuarry and I will purchase them once you are selected as the winning design)
- Link to a loan calculator somewhere on front page with a button 'Find out how much you could borrow' (or maybe even try adding a loan calculator to the homepage if you think this would look good)
- Page should have a main headline "Finding the right loan for you" or "Brightwell Lending finds the right loan for our customers."
- Must include Accreditation logos somewhere on the homepage (will try and supply these soon)
Should not have
• - Poor quality designs will not be considered
- Do not use clipart

```html
<!DOCTYPE html>
<html lang="en">
<head>
<meta charset="utf-8">
<title>Brightwell Lending</title>
<link href="https://fonts.googleapis.com/css2?family=Arimo:wght@400;700&display=swap" rel="stylesheet">
<style>
  :root {
    --cyan: #2eade3;
    --cyan-light: #62d3f7;
    --blue: #004b70;
    --band-top: #3aa3cf;
    --band-bottom: #17709a;
    --page-bg: #efefef;
    --ink: #2b2b2b;
    --muted: #8a8a8a;
    --item: #555;
    --white: #ffffff;
  }
  * { box-sizing: border-box; margin: 0; padding: 0; }
  html, body { width: 1200px; height: 897px; overflow: hidden; }
  body {
    position: relative;
    font-family: "Arimo", Arial, sans-serif;
    background: radial-gradient(ellipse at 50% 35%, #fbfbfb 0%, var(--page-bg) 70%);
    color: var(--ink);
  }
  a { color: inherit; text-decoration: none; }

  .brand {
    position: absolute; left: 125px; top: 62px;
    display: flex; align-items: center; gap: 10px;
  }
  .brand-mark { width: 26px; height: 26px; border-radius: 50%; background: var(--cyan); }
  .brand-name { font-size: 33px; font-weight: 400; color: var(--cyan); letter-spacing: -0.5px; }

  .call-box {
    position: absolute; left: 779px; top: 30px; width: 295px; height: 67px;
    border-radius: 8px;
    background: linear-gradient(#4eb3d8, #2a86b1);
    box-shadow: 0 2px 4px rgba(0,0,0,.25);
    color: var(--white);
  }
  .call-box .line1 { position: absolute; left: 18px; top: 12px; font-size: 12px; }
  .call-box .line1 strong { font-size: 19px; font-weight: 400; margin-left: 8px; }
  .call-box .line2 { position: absolute; left: 18px; top: 37px; font-size: 12px; }
  .call-box .go { position: absolute; right: 20px; top: 16px; }

  .main-nav {
    position: absolute; left: 119px; top: 125px; width: 960px; height: 44px;
    border-radius: 5px 5px 0 0;
    background: linear-gradient(var(--band-top), var(--band-bottom));
    display: flex; align-items: center;
    font-size: 13px; color: var(--white);
  }
  .main-nav a { position: absolute; top: 16px; }
  .main-nav .current { font-weight: 700; }
  .main-nav .active { color: var(--cyan-light); font-weight: 700; }

  .hero {
    position: absolute; left: 119px; top: 175px; width: 960px; height: 254px;
    border-radius: 4px;
    background: linear-gradient(#a6def3, #5dbde3);
    overflow: hidden;
  }
  .hero-photo {
    position: absolute; left: 0; top: 0; width: 380px; height: 254px;
    background: linear-gradient(160deg, #bfe6f6 0%, #d9b79a 45%, #b88966 100%);
  }
  .hero-panel {
    position: absolute; left: 402px; top: 10px; width: 548px; height: 232px;
    border-radius: 5px;
    background: rgba(150, 215, 240, .75);
  }
  .hero-panel h1 {
    position: absolute; left: 17px; top: 16px; width: 500px;
    font-size: 24px; font-weight: 400; line-height: 30px;
    color: #3e4a52; text-transform: uppercase; letter-spacing: .5px;
  }
  .hero-panel .copy {
    position: absolute; left: 14px; top: 89px; width: 521px;
    font-size: 11px; line-height: 14px; text-align: justify; color: #1f2a30;
  }
  .hero-panel .copy p + p { margin-top: 14px; }
  .hero-panel .copy .lead { text-indent: 34px; }

  .service { position: absolute; top: 449px; width: 212px; }
  .service h2 {
    text-align: center; font-size: 18px; font-weight: 400;
    color: var(--muted); letter-spacing: 1px; text-transform: uppercase;
    margin-left: -20px; margin-right: -20px;
  }
  .service-card {
    position: absolute; top: 32px; left: 0; width: 212px; height: 142px;
    border: 1px solid #dcdcdc; border-radius: 9px;
    background: linear-gradient(#ffffff 55%, #eeeeee);
    box-shadow: 0 9px 8px -6px rgba(0,0,0,.3);
    padding: 20px 0 0 18px;
    list-style: none;
    font-size: 12px; color: var(--item); letter-spacing: .3px;
  }
  .service-card li { height: 30px; display: flex; align-items: flex-start; }
  .service-card li::before {
    content: ""; width: 0; height: 0; margin: 3px 8px 0 0; flex: none;
    border-left: 6px solid var(--cyan);
    border-top: 3.5px solid transparent; border-bottom: 3.5px solid transparent;
  }
  .service-card li.plain::before { border-left-color: transparent; }
  .service-card li.title { font-weight: 700; padding-left: 28px; }
  .service-card li.title::before { display: none; }
  .service-card.indent { padding-left: 28px; }

  .divider {
    position: absolute; left: 119px; top: 655px; width: 960px; height: 1px;
    background: linear-gradient(90deg, transparent, #cfcfcf 15%, #cfcfcf 85%, transparent);
  }
  .accreditations { position: absolute; left: 0; top: 666px; width: 1200px; height: 116px; }

  .site-footer {
    position: absolute; left: 119px; top: 797px; width: 960px; height: 100px;
    border-radius: 6px 6px 0 0;
    background: linear-gradient(var(--band-top), var(--band-bottom));
    color: var(--white); font-size: 11px; letter-spacing: .6px;
  }
  .footer-links { position: absolute; left: 25px; top: 45px; display: flex; gap: 0; }
  .footer-links a + a::before { content: "|"; margin: 0 9px; }
  .copyright { position: absolute; right: 21px; top: 45px; }
</style>
</head>
<body>

<header>
  <a class="brand" href="#">
    <span class="brand-mark"></span>
    <span class="brand-name">Brightwell Lending</span>
  </a>
  <a class="call-box" href="#">
    <span class="line1">Call us now at <strong>1800 555 214</strong></span>
    <span class="line2">to choose the right loan for you</span>
    <svg class="go" width="34" height="34" viewBox="0 0 34 34" aria-hidden="true">
      <circle cx="17" cy="17" r="16" fill="#7dd3f2" stroke="#cdeffb" stroke-width="1.5"/>
      <path d="M9 14h8v-5l8 8-8 8v-5H9z" fill="#ffffff"/>
    </svg>
  </a>
</header>

<nav class="main-nav">
  <a class="current" href="#" style="left:15px">Home</a>
  <a class="active" href="#" style="left:80px">Services</a>
  <a href="#" style="left:168px">About Us</a>
  <a href="#" style="left:253px">FAQ</a>
  <a href="#" style="left:308px">Contact Us</a>
</nav>

<section class="hero">
  <div class="hero-photo" role="img" aria-label="Stock photo of a smiling family of four (PixQuarry)"></div>
  <div class="hero-panel">
    <h1>Brightwell Lending finds the right loan for our customers</h1>
    <div class="copy">
      <p class="lead">At Brightwell Lending we work hard to find the right loan for our customers. We do that because we are backed by sound industry knowledge, professional experience and a great customer service approach.</p>
      <p>Brightwell Lending guarantees that we will always tailor the best solution for your individual lending needs.</p>
      <p>We can do that because we have access to a wide variety of lending options from major banks to non-bank lenders and we are committed to finding the right lending product for you.</p>
    </div>
  </div>
</section>

<section class="service" style="left:131px">
  <h2>Home Loan</h2>
  <ul class="service-card">
    <li>Home buyers</li>
    <li>First home buyers</li>
    <li>Over 20 lenders</li>
  </ul>
</section>
<section class="service" style="left:371px">
  <h2>Investment Loan</h2>
  <ul class="service-card">
    <li>Property investment loans</li>
    <li>Interest only loans</li>
  </ul>
</section>
<section class="service" style="left:611px">
  <h2>Refinancing</h2>
  <ul class="service-card">
    <li>Refinancing for the best rate</li>
    <li>Upsizing or downsizing</li>
    <li>Change from a variable</li>
    <li class="plain">to a fixed rate</li>
  </ul>
</section>
<section class="service" style="left:851px">
  <h2>Business Loan</h2>
  <ul class="service-card">
    <li class="title">Business Finance</li>
    <li style="padding-left:10px">Long term</li>
    <li style="padding-left:10px">Short term</li>
    <li style="padding-left:10px">Equipment and Leasing</li>
  </ul>
</section>

<div class="divider"></div>

<svg class="accreditations" viewBox="0 666 1200 116" aria-label="Accreditation badges">
  <rect x="169" y="689" width="203" height="74" rx="3" fill="#ffffff" stroke="#1d5f92" stroke-width="4"/>
  <rect x="175" y="695" width="191" height="62" fill="#e6f1f8"/>
  <circle cx="457" cy="724" r="52" fill="#3a3a3a"/>
  <circle cx="457" cy="724" r="40" fill="#ffffff"/>
  <circle cx="578" cy="727" r="50" fill="#1563b0"/>
  <circle cx="578" cy="727" r="42" fill="none" stroke="#ffffff" stroke-width="2"/>
  <circle cx="700" cy="725" r="48" fill="#ffffff" stroke="#222" stroke-width="2"/>
  <circle cx="700" cy="725" r="30" fill="#d8d8d8"/>
  <circle cx="845" cy="724" r="48" fill="#ffffff" stroke="#c9302c" stroke-width="1.5"/>
  <circle cx="991" cy="722" r="54" fill="#1f9a2a"/>
  <circle cx="991" cy="722" r="36" fill="none" stroke="#ffffff" stroke-width="2"/>
</svg>

<footer class="site-footer">
  <nav class="footer-links">
    <a href="#">Home</a>
    <a href="#">Services</a>
    <a href="#">About Us</a>
    <a href="#">FAQ</a>
    <a href="#">Terms &amp; Conditions</a>
    <a href="#">Privacy Policy</a>
    <a href="#">Contact Us</a>
  </nav>
  <p class="copyright">Copyright © 2012. Brightwelllending.com</p>
</footer>

</body>
</html>
```